Brick nest business card for client

Require a business card design for a new company based in Trinidad & Tobago called "Brick nest".

We source building supplies for resident and commercial projects. We manage and supply all your building solutions.

Exp: If you was to build a house or commercial building, My company Brick nest will supply and install all your building needs. Floor tile, Windows, Door, Molding .

Target Market(s)

Construction client

Industry/Entity Type

Building

Contact Information for Business Card

BRICK NEST LIMITED
VERDANT TRADE COURT
LA PALMERA, EXT. NO. 4, BLDG 3
SAN JUAN, TRINIDAD, W.I.
868-642-9087
bricknestlimited.example
derek@bricknestlimited.example

Font styles to use
Serif

Requirements
Must have
• Company name
• Address
• My Name: Derek Rampersook
• Director
Nice to have
• Modern business card (With a new logo)

```html
<!DOCTYPE html>
<html lang="en">
<head>
<meta charset="utf-8">
<title>Brick Nest Limited – Business Card</title>
<link href="https://fonts.googleapis.com/css2?family=Playfair+Display:wght@500&family=Montserrat:wght@400;600&display=swap" rel="stylesheet">
<style>
  :root {
    --backdrop: #e6e4e1;
    --card: #ffffff;
    --navy: #141c2c;
    --gold: #e2b56f;
    --ink: #2a2f38;
    --muted: #5b6270;
    --paper-edge: #d9d9d9;
  }
  * { margin: 0; padding: 0; box-sizing: border-box; }
  html, body {
    width: 1200px; height: 900px; overflow: hidden;
    background: var(--backdrop);
  }
  .canvas {
    width: 1200px; height: 900px;
    display: flex; flex-direction: column;
    align-items: center; justify-content: center; gap: 40px;
  }
  .card {
    position: relative;
    width: 700px; height: 400px;
    background: var(--card);
    border-radius: 34px;
    overflow: hidden;
    box-shadow: 0 2px 0 var(--paper-edge), 0 12px 28px rgba(0,0,0,0.12);
    font-family: "Montserrat", sans-serif;
    color: var(--ink);
  }
  .card__wave { position: absolute; inset: 0; width: 100%; height: 100%; }

  .contact {
    position: absolute; left: 46px; top: 40px;
    font-size: 13px; line-height: 1.35;
  }
  .contact__address { margin-bottom: 10px; font-weight: 600; }
  .contact__row { display: flex; align-items: center; gap: 10px; margin-top: 6px; }
  .contact__icon { width: 14px; height: 14px; fill: var(--muted); flex: none; }

  .brand {
    position: absolute; left: 340px; top: 128px;
    display: flex; align-items: center; gap: 14px;
  }
  .brand__mark { width: 26px; height: 26px; background: var(--gold); flex: none; }
  .brand__name {
    font-family: "Playfair Display", serif; font-weight: 500;
    font-size: 48px; line-height: 1; color: var(--ink);
    white-space: nowrap;
  }

  .person {
    position: absolute; right: 60px; bottom: 34px;
    text-align: right; color: #ffffff;
  }
  .person__name { font-size: 17px; font-weight: 600; letter-spacing: 1px; }
  .person__role { font-size: 14px; margin-top: 4px; }

  .card--back .brand { left: 50%; top: 50%; transform: translate(-50%, -50%); }
</style>
</head>
<body>
<main class="canvas">

  <section class="card card--front">
    <svg class="card__wave" viewBox="0 0 700 400" preserveAspectRatio="none" aria-hidden="true">
      <path d="M0,190 C160,265 420,300 700,262 L700,280 C420,318 160,290 0,214 Z" fill="var(--gold)"/>
      <path d="M0,222 C160,300 430,330 700,292 L700,400 L0,400 Z" fill="var(--navy)"/>
    </svg>

    <div class="contact">
      <p class="contact__address">Verdant Trade Court<br>La Palmera, Ext. No. 4, Bldg 3</p>
      <p class="contact__row">
        <svg class="contact__icon" viewBox="0 0 24 24" aria-hidden="true"><path d="M6.6 10.8a15.1 15.1 0 0 0 6.6 6.6l2.2-2.2a1 1 0 0 1 1-.25 11.4 11.4 0 0 0 3.6.57 1 1 0 0 1 1 1V20a1 1 0 0 1-1 1A17 17 0 0 1 3 4a1 1 0 0 1 1-1h3.5a1 1 0 0 1 1 1c0 1.25.2 2.45.57 3.57a1 1 0 0 1-.25 1z"/></svg>
        868-642-9087
      </p>
      <p class="contact__row">
        <svg class="contact__icon" viewBox="0 0 24 24" aria-hidden="true"><path d="M12 2a10 10 0 1 0 0 20 10 10 0 0 0 0-20zm6.9 6h-2.9a15.7 15.7 0 0 0-1.4-3.6A8 8 0 0 1 18.9 8zM12 4c.8 1.2 1.5 2.5 1.9 4h-3.8c.4-1.5 1.1-2.8 1.9-4zM4.3 14a8 8 0 0 1 0-4h3.4a16.5 16.5 0 0 0 0 4zm.8 2h2.9c.3 1.3.8 2.5 1.4 3.6A8 8 0 0 1 5.1 16zM8 8H5.1a8 8 0 0 1 4.3-3.6C8.8 5.5 8.4 6.7 8 8zm4 12c-.8-1.2-1.5-2.5-1.9-4h3.8c-.4 1.5-1.1 2.8-1.9 4zm2.3-6H9.7a14.7 14.7 0 0 1 0-4h4.6a14.7 14.7 0 0 1 0 4zm.3 5.6c.6-1.1 1.1-2.3 1.4-3.6h2.9a8 8 0 0 1-4.3 3.6zm1.7-5.6a16.5 16.5 0 0 0 0-4h3.4a8 8 0 0 1 0 4z"/></svg>
        bricknestlimited.example
      </p>
      <p class="contact__row">
        <svg class="contact__icon" viewBox="0 0 24 24" aria-hidden="true"><path d="M20 4H4a2 2 0 0 0-2 2v12a2 2 0 0 0 2 2h16a2 2 0 0 0 2-2V6a2 2 0 0 0-2-2zm0 4-8 5-8-5V6l8 5 8-5z"/></svg>
        derek@bricknestlimited.example
      </p>
    </div>

    <div class="brand">
      <span class="brand__mark" aria-hidden="true"></span>
      <span class="brand__name">Brick Nest</span>
    </div>

    <div class="person">
      <p class="person__name">DEREK RAMPERSOOK</p>
      <p class="person__role">Director</p>
    </div>
  </section>

  <section class="card card--back">
    <div class="brand">
      <span class="brand__mark" aria-hidden="true"></span>
      <span class="brand__name">Brick Nest</span>
    </div>
  </section>

</main>
</body>
</html>
```